Copper Lark Treks Flyer

I have an adventure travel company and I need a flyer to promote my trip to Ukraine.
I would like to have a universal flyer that I can change based on the trip.
The Title should say "Travel to Ukraine: 9 Day Eastern European Adventure"
The date should be under the title.
The background photo should be kiev2.jpg
The highlights of the trip, then price $1200 and what it includes. See the text for highlights and includes sections here:
http://www.copperlarktreks.com/#!featured-trip
The website link (www.copperlarktreks.com) should be somewhere in the bottom.
You can use other photos provided or from my website that relates to Ukraine trip.

```html
<!DOCTYPE html>
<html lang="en">
<head>
<meta charset="utf-8">
<title>Copper Lark Treks – Travel to Ukraine</title>
<link href="https://fonts.googleapis.com/css2?family=Arimo:wght@400;700&family=Archivo+Black&display=swap" rel="stylesheet">
<style>
  :root {
    --accent: #f7e20c;
    --white: #ffffff;
    --base-grey: #474747;
    --panel: rgba(70, 70, 70, 0.72);
    --frame: #f4f4f4;
  }
  * { margin: 0; padding: 0; box-sizing: border-box; }
  html, body { width: 931px; height: 1200px; overflow: hidden; background: var(--base-grey); }
  .flyer {
    position: relative; width: 931px; height: 1200px; overflow: hidden;
    background: var(--base-grey);
    font-family: "Arimo", Arial, sans-serif; color: var(--white);
  }
  .hero-photo {
    position: absolute; left: 0; top: 0; width: 931px; height: 745px;
    background:
      linear-gradient(180deg, #8fa9c4 0%, #9cb3c7 6%, #6f8a7a 11%, #3f5c3a 15%, #6f8797 18%, #5d7890 24%, #42603a 29%, #4d6a3c 45%, #7a7f6e 60%, #6d6a5e 80%, #8b7d6a 100%);
  }
  .hero-photo::after {
    content: ""; position: absolute; left: 330px; top: 40px; width: 380px; height: 700px;
    background: radial-gradient(ellipse at 50% 45%, rgba(214,178,70,0.55), rgba(214,178,70,0) 65%);
  }
  .title-box {
    position: absolute; left: 54px; top: 33px; width: 819px; height: 146px;
    background: var(--panel);
  }
  .title {
    position: absolute; left: 86px; top: 60px;
    font-family: "Archivo Black", "Arial Black", sans-serif; font-size: 36px; line-height: 48px;
    text-shadow: 1px 1px 2px rgba(0,0,0,0.5);
  }
  .title .line2 { display: block; padding-left: 11px; }
  .accent { color: var(--accent); }
  .highlights {
    position: absolute; left: 27px; top: 292px; width: 753px; height: 404px;
    background: var(--panel); padding: 36px 0 0 26px;
  }
  .section-head { font-family: "Arimo", Arial, sans-serif; font-weight: 700; font-size: 26px; }
  .highlight-list { list-style: none; margin-top: 23px; font-size: 21px; line-height: 29.5px; letter-spacing: -0.4px; }
  .highlight-list b { color: var(--accent); font-weight: 700; }
  .snapshot {
    position: absolute; background: var(--frame); padding: 10px;
    box-shadow: 2px 4px 8px rgba(0,0,0,0.45);
  }
  .snapshot .shot { width: 100%; height: 100%; position: relative; }
  .snapshot .caption {
    position: absolute; left: 8px; bottom: 14px; font-weight: 700; font-size: 19px;
    text-shadow: 1px 1px 3px rgba(0,0,0,0.8);
  }
  .snap-ghost { left: 32px; top: 712px; width: 286px; height: 222px; transform: rotate(2deg); }
  .snap-ghost .shot { background: linear-gradient(170deg, #b9cbd8 0%, #8da2ad 40%, #6b7a6e 70%, #4d5a3f 100%); }
  .snap-crimea { left: 332px; top: 708px; width: 272px; height: 222px; transform: rotate(-2deg); }
  .snap-crimea .shot { background: linear-gradient(180deg, #5f6f80 0%, #9aa8b5 25%, #2f6f86 45%, #4b6e3e 70%, #3f5530 100%); }
  .snap-caves { left: 615px; top: 714px; width: 292px; height: 222px; transform: rotate(3deg); }
  .snap-caves .shot { background: radial-gradient(ellipse at 50% 45%, #e7c79a 0%, #b98a55 45%, #6a4526 100%); }
  .included { position: absolute; left: 49px; top: 930px; }
  .included-list { list-style: none; margin-top: 30px; font-size: 21px; line-height: 28.5px; letter-spacing: -0.3px; }
  .price {
    position: absolute; left: 436px; top: 950px;
    font-family: "Archivo Black", "Arial Black", sans-serif; font-size: 66px; line-height: 80px;
    color: var(--accent); text-shadow: 2px 2px 4px rgba(0,0,0,0.5);
  }
  .website {
    position: absolute; right: 62px; top: 1143px;
    font-weight: 700; font-size: 23px; color: var(--accent);
  }
</style>
</head>
<body>
<main class="flyer">
  <div class="hero-photo" role="img" aria-label="Aerial view of golden-domed Kyiv monastery churches above the Dnipro river and green city skyline"></div>

  <div class="title-box"></div>
  <h1 class="title">Travel to <span class="accent">Ukraine</span>:<span class="line2">9 Day Eastern European Adventure</span></h1>

  <section class="highlights">
    <h2 class="section-head">Highlights:</h2>
    <ul class="highlight-list">
      <li><b>Discover Kiev</b>- the birthplace of Eastern Slavic Civilization</li>
      <li>Meet Crimea's fascinating <b>Tatar Minority</b> in Bakhchysaray - former capital of Crimean Tatar Khans</li>
      <li><b>Walk to Chufut-Kale</b> - Crimea's best preserved&nbsp; medieval cave town</li>
      <li>Hike in the most spectacular areas in <b>Karabi</b> and explore the caves with a group of professional speleologist</li>
      <li>Inhale the magic <b>Yalta's air</b>- an invigorating blend of sea and pine forest sprinkled with mountain chill</li>
      <li><b>Visit Odessa</b> - "the Pearl by the Black Sea", Catacombs, Opera house, the factory of sparkling wines and famous Potemkin Steps</li>
    </ul>
  </section>

  <figure class="snapshot snap-ghost">
    <div class="shot" role="img" aria-label="Rocky mountain ridge with a lone pine tree in Ghost Valley"></div>
    <figcaption class="caption">Ghost Valley</figcaption>
  </figure>
  <figure class="snapshot snap-crimea">
    <div class="shot" role="img" aria-label="Crimean coastline with green hills and blue sea under clouds"></div>
    <figcaption class="caption">Crimea</figcaption>
  </figure>
  <figure class="snapshot snap-caves">
    <div class="shot" role="img" aria-label="Amber cave interior with stalactites and crystal formations"></div>
    <figcaption class="caption">Cold caves</figcaption>
  </figure>

  <section class="included">
    <h2 class="section-head">Included:</h2>
    <ul class="included-list">
      <li>9 nights accommodations</li>
      <li>Breakfast, lunch and dinner daily</li>
      <li>English speaking tour guides and transportation at every destination.</li>
      <li>Tour leader from USA at all times during the trip.</li>
      <li>All Group Transfers (trains, buses and vans),&nbsp; sightseeing tours and entrance fees</li>
    </ul>
  </section>

  <p class="price">Price $1200</p>
  <p class="website">www.copperlarktreks.com</p>
</main>
</body>
</html>
```